Exclusive Furniture Company
Relunda GmbH
Project: Exclusive Furniture Company
Exclusive Furniture Company - General Merchandise
Creative Brief
Professional
Tarin HOLDEVA
CEO
Wolkenriedstrasse 4 8124 Lindwiler - Zürich Switzerland
t.tarin@relunda.ch
www.relunda.ch
Only the symbol R from Logo
Sarah2014 Sarah2014
Dear Designers I need Business Card and Stationary! (not only Business Cards) Thanks in advance Greta
Dear Designer, Please try the black color in other color variants... Thanks in advance! Greta
Dear Designer, Back of the business card is OK Fron part only with logo! see atachemnt: http://relunda.ch/logo/business-card-relunda.png Thanks in advance! Greta PS: I apologize for my English mistakes.

```html
<!DOCTYPE html>
<html lang="en">
<head>
<meta charset="utf-8">
<title>Relunda GmbH – Business Card</title>
<link href="https://fonts.googleapis.com/css2?family=Exo+2:wght@400;500&display=swap" rel="stylesheet">
<style>
  :root {
    --backdrop: #e4e4e4;
    --card: #ffffff;
    --ink: #2a2a2a;
    --ink-soft: #4a4a4a;
    --accent: #c8141f;
    --avatar: #707070;
  }
  * { margin: 0; padding: 0; box-sizing: border-box; }
  html, body {
    width: 1200px; height: 816px; overflow: hidden;
    background: var(--backdrop);
    font-family: "Exo 2", sans-serif;
  }
  .card {
    position: absolute; left: 70px; top: 105px;
    width: 1060px; height: 606px;
    background: var(--card);
    border-radius: 48px;
    box-shadow: 0 10px 30px rgba(0,0,0,.12);
  }
  .rule { position: absolute; height: 4px; background: var(--ink); }
  .rule--top { left: 170px; top: 168px; width: 320px; }
  .rule--bottom { left: 110px; top: 290px; width: 390px; }

  .identity { position: absolute; left: 110px; top: 195px; display: flex; align-items: center; gap: 22px; }
  .avatar { width: 46px; height: 46px; }
  .identity__name { font-size: 28px; font-weight: 500; color: var(--ink); letter-spacing: 1px; line-height: 1.15; }
  .identity__title { font-size: 24px; color: var(--ink-soft); letter-spacing: 1.5px; line-height: 1.15; }

  .contacts { position: absolute; left: 150px; top: 340px; list-style: none; }
  .contact { display: flex; align-items: center; gap: 22px; height: 78px; }
  .contact__icon { width: 44px; height: 44px; flex: none; }
  .contact__text { font-size: 22px; color: var(--ink); line-height: 1.2; letter-spacing: .5px; }

  .brand { position: absolute; left: 660px; top: 268px; display: flex; align-items: center; gap: 18px; }
  .brand__mark { width: 34px; height: 34px; background: var(--accent); }
  .brand__name { font-size: 60px; font-weight: 500; color: var(--ink); letter-spacing: 4px; }
</style>
</head>
<body>
  <main class="card">
    <div class="rule rule--top"></div>

    <div class="identity">
      <svg class="avatar" viewBox="0 0 46 46" aria-hidden="true">
        <circle cx="23" cy="23" r="23" fill="var(--avatar)"/>
        <circle cx="23" cy="18" r="7" fill="#fff"/>
        <path d="M11 35c2-7 7-10 12-10s10 3 12 10z" fill="#fff"/>
      </svg>
      <div>
        <p class="identity__name">TARIN HOLDEVA</p>
        <p class="identity__title">Managing Director</p>
      </div>
    </div>

    <div class="rule rule--bottom"></div>

    <ul class="contacts">
      <li class="contact">
        <svg class="contact__icon" viewBox="0 0 44 44" aria-hidden="true">
          <circle cx="22" cy="22" r="22" fill="var(--accent)"/>
          <rect x="15" y="10" width="14" height="24" rx="2.5" fill="none" stroke="#fff" stroke-width="2.5"/>
          <circle cx="22" cy="29.5" r="1.6" fill="#fff"/>
        </svg>
        <p class="contact__text">044 512 3870<br>079 268 4415</p>
      </li>
      <li class="contact">
        <svg class="contact__icon" viewBox="0 0 44 44" aria-hidden="true">
          <circle cx="22" cy="22" r="22" fill="var(--accent)"/>
          <rect x="11" y="12" width="22" height="15" rx="1.5" fill="none" stroke="#fff" stroke-width="2.5"/>
          <path d="M18 32h8M22 27v5" stroke="#fff" stroke-width="2.5"/>
        </svg>
        <p class="contact__text">t.tarin@relunda.ch<br>www.relunda.ch</p>
      </li>
      <li class="contact">
        <svg class="contact__icon" viewBox="0 0 44 44" aria-hidden="true">
          <circle cx="22" cy="22" r="22" fill="var(--accent)"/>
          <path d="M22 34s-8-9-8-15a8 8 0 0 1 16 0c0 6-8 15-8 15z" fill="#fff"/>
          <circle cx="22" cy="19" r="3" fill="var(--accent)"/>
        </svg>
        <p class="contact__text">Wolkenriedstrasse 4,<br>8124 Lindwiler</p>
      </li>
    </ul>

    <div class="brand">
      <span class="brand__mark"></span>
      <span class="brand__name">RELUNDA</span>
    </div>
  </main>
</body>
</html>
```